Homes available for sale in Bethel Alaska

For Sale, Bethel Alaska

318 Parvel Street
$215,000
SF Lot: 4,787
This home is 1,140 SF with 3 bedrooms, 1 bath, plus a scuttle attic. Located within the Pelvigoranq subdivision.

562 Quarry Fern Road
$215,000
SF Lot: 5,077
This home is 1,152 SF with 3 bedrooms, 1 bath. A great single family in close proximity
to the Kuskokwin River.

7413 Dovinquet
$199,000
SF Lot: 10,140
This ranch style duplex is located within the Copper Hollow subdivision.
Unit #1 has 2 bedrooms 1 bath and 896 SF of living space.
Unit #2 has 1 bedroom 1 bath and 672 SF of living space.

2087 Hobart's Way
$295,000
SF Lot: 16,611
This ranch style duplex is located within the Nuvadrel subdivision.
Each unit has 1,040 SF of living space, 3 bedrooms, 2 baths, plus a small patio deck.

2094 Hobart's Way
$340,000
SF Lot: 10,250
Fantastic 2 story located with the Whitcombe subdivision.
Unit #1 has 3 bedrooms, 1.5 bath's and 1,183 SF of living space.
Unit #2 has 2 bedrooms, 1.5 baths' and 967 SF of living space.

Contact Info

Gordon Dalby
Office: 907-413-2097
Cell: 907-356-1942
Gordon@[url removed, login to view]

Hattie Dalby
Office: 907-413-2097
Cell: 907-584-6071
Hattie@[url removed, login to view]

```html
<!DOCTYPE html>
<html lang="en">
<head>
<meta charset="utf-8">
<title>Homes For Sale – Bethel Alaska</title>
<link href="https://fonts.googleapis.com/css2?family=Arimo:wght@400;700&family=Archivo+Narrow:wght@400;700&family=Libre+Baskerville:wght@700&family=Lobster&display=swap" rel="stylesheet">
<style>
  :root{
    --red:#a3101a;
    --red-dark:#7d0a12;
    --title-red:#9b1118;
    --ink:#1e1e1e;
    --grey:#6d6d6d;
    --white:#ffffff;
  }
  *{margin:0;padding:0;box-sizing:border-box}
  html,body{width:848px;height:1200px;overflow:hidden;background:var(--white)}
  .flyer{position:relative;width:848px;height:1200px;overflow:hidden;background:var(--white);font-family:Arimo,Arial,sans-serif;color:var(--ink)}

  .header-band{position:absolute;left:0;top:0;width:848px;height:158px;
    background:linear-gradient(90deg,var(--red) 0%,var(--red) 8%,rgba(163,16,26,.35) 30%,var(--white) 50%)}
  .headline{position:absolute;left:83px;top:6px;font-family:"Libre Baskerville",Georgia,serif;font-weight:700;font-size:44px;
    color:#4e4e4e;letter-spacing:.5px;
    text-shadow:-2px -2px 0 #fff,2px -2px 0 #fff,-2px 2px 0 #fff,2px 2px 0 #fff,3px 4px 4px rgba(0,0,0,.45)}
  .subhead{position:absolute;left:240px;top:56px;font-family:Lobster,cursive;font-size:40px;color:var(--red);
    text-shadow:-2px -2px 0 #fff,2px -2px 0 #fff,-2px 2px 0 #fff,2px 2px 0 #fff,3px 4px 4px rgba(0,0,0,.4)}
  .intro{position:absolute;left:579px;top:24px;width:262px;font-size:12.5px;line-height:16.5px;text-indent:22px}

  .row{position:absolute;left:0;width:848px}
  .row--photo-left{background:linear-gradient(90deg,var(--white) 0%,var(--white) 62%,var(--red) 82%,var(--red) 100%)}
  .row--photo-right{background:linear-gradient(90deg,var(--red) 0%,var(--red) 10%,rgba(163,16,26,.4) 26%,var(--white) 38%)}

  .bethel-mark{position:absolute;left:285px;top:440px;width:450px;height:250px;border-radius:50%;
    background:radial-gradient(ellipse at center,rgba(150,150,170,.22) 0%,rgba(150,150,170,0) 70%)}

  .photo{position:absolute;width:255px;height:165px;border:3px solid var(--white);
    box-shadow:1px 2px 5px rgba(0,0,0,.5)}
  .photo--sky{background:linear-gradient(180deg,#dfe3e8 0%,#cfd6de 45%,#7fa8c2 60%,#8b8060 80%,#6e6048 100%)}
  .photo--tall{background:linear-gradient(180deg,#e4e6ea 0%,#d9dde2 25%,#5b9ac7 45%,#4d8fc0 70%,#7c6c4c 100%)}
  .photo--white{background:linear-gradient(180deg,#f1f2f4 0%,#e6e7ea 40%,#cfd0d2 75%,#6f6a58 100%)}
  .photo--yellow{background:linear-gradient(180deg,#e7eaee 0%,#dcdfe4 40%,#b7a56a 60%,#7d6f50 80%,#5e5440 100%)}

  .price{position:absolute;width:136px;height:33px;background:var(--red);border:3px solid var(--white);border-bottom:none;
    color:var(--white);font-weight:700;font-size:18.5px;line-height:30px;text-align:center;box-shadow:1px -1px 4px rgba(0,0,0,.35)}

  .listing{position:absolute;left:297px;width:262px;font-size:12.5px;line-height:16.5px}
  .listing h2{font-size:17px;font-weight:700;color:var(--title-red);letter-spacing:.3px;margin-bottom:5px}
  .listing .lot{font-size:11.5px;font-weight:700;color:var(--grey);margin-bottom:8px}
  .listing--left .lot{padding-left:42px}
  .listing--right h2{text-align:right}
  .listing--right .lot{text-align:right;padding-right:70px}

  .web-bar{position:absolute;left:0;top:1016px;width:848px;height:44px;
    background:linear-gradient(180deg,var(--red) 0%,var(--red-dark) 100%);text-align:center}
  .web-bar span{font-weight:700;font-size:30px;line-height:44px;color:#5a5a5a;letter-spacing:.5px;
    text-shadow:-2px -2px 0 #fff,2px -2px 0 #fff,-2px 2px 0 #fff,2px 2px 0 #fff,2px 3px 3px rgba(0,0,0,.4)}

  .contact-title{position:absolute;left:34px;top:1066px;font-family:"Archivo Narrow",Arial,sans-serif;font-weight:700;font-size:18px}
  .agent{position:absolute;top:1095px;font-family:"Archivo Narrow",Arial,sans-serif;font-size:19px;line-height:22.5px}
  .agent--left{left:30px}
  .agent--right{left:604px}

  .brokerage{position:absolute;left:282px;top:1108px;width:294px}
  .brokerage-name{display:flex;align-items:center;gap:8px;font-weight:700;font-size:22px;color:var(--red);letter-spacing:.5px}
  .brokerage-name i{display:block;width:18px;height:18px;background:var(--red)}
  .brokerage-address{font-size:8px;color:var(--ink);margin-top:4px;padding-left:26px}
</style>
</head>
<body>
<div class="flyer">
  <div class="header-band"></div>
  <h1 class="headline">Homes For Sale</h1>
  <div class="subhead">Bethel Alaska</div>
  <p class="intro">Great commercial double lot on Crane Marsh Highway across from the fire station and Bethel city offices. Two dilapidated houses could be renovated goes with the deal. Ready to build on only $250,000</p>

  <div class="row row--photo-left" style="top:158px;height:167px"></div>
  <div class="row row--photo-right" style="top:325px;height:170px"></div>
  <div class="row row--photo-left" style="top:495px;height:167px"></div>
  <div class="row row--photo-right" style="top:662px;height:167px"></div>
  <div class="row row--photo-left" style="top:829px;height:169px"></div>

  <div class="bethel-mark" role="img" aria-label="Faint large Bethel script lettering behind the listings"></div>

  <!-- Listing 1 -->
  <div class="price" style="left:133px;top:127px">$ 199,000</div>
  <div class="photo photo--sky" style="left:13px;top:159px" role="img" aria-label="Photo of a blue ranch style duplex on stilts on tundra"></div>
  <div class="listing listing--left" style="top:163px">
    <h2>7413 Dovinquet</h2>
    <p class="lot">SF Lot: 10,140</p>
    <p>This ranch style duplex is located within the Copper Hollow subdivision.<br>Unit #1 has 2 bedrooms 1 bath and 896 SF of living space.<br>Unit #2 has 1 bedroom 1 bath and 672 SF of living space.</p>
  </div>

  <!-- Listing 2 -->
  <div class="price" style="left:577px;top:297px">$ 215,000</div>
  <div class="photo photo--tall" style="left:577px;top:328px" role="img" aria-label="Photo of a small blue A-frame home with red window trim"></div>
  <div class="listing listing--right" style="top:328px">
    <h2>562 Quarry Fern Road</h2>
    <p class="lot">SF Lot: 5,077</p>
    <p>This home is 1,152 SF with 3 bedrooms, 1 bath. A great single family in close proximity to the Kuskokwin River.</p>
  </div>

  <!-- Listing 3 -->
  <div class="price" style="left:133px;top:466px">$ 215,000</div>
  <div class="photo photo--white" style="left:13px;top:497px" role="img" aria-label="Photo of a white home with a blue metal roof"></div>
  <div class="listing listing--left" style="top:498px">
    <h2>318 Parvel Street</h2>
    <p class="lot">SF Lot: 4,787</p>
    <p>This home is 1,140 SF with 3 bedrooms, 1 bath, plus a scuttle attic. Located within the Pelvigoranq subdivision.</p>
  </div>

  <!-- Listing 4 -->
  <div class="price" style="left:577px;top:631px">$ 295,000</div>
  <div class="photo photo--yellow" style="left:577px;top:662px" role="img" aria-label="Photo of a long yellow ranch style duplex with a deck"></div>
  <div class="listing listing--right" style="top:664px">
    <h2>2087 Hobart's Way</h2>
    <p class="lot">SF Lot: 16,611</p>
    <p>This ranch style duplex is located within the Nuvadrel subdivision.<br>Each unit has 1,040 SF of living space, 3 bedrooms, 2 baths, plus a small patio deck.</p>
  </div>

  <!-- Listing 5 -->
  <div class="price" style="left:133px;top:798px">$ 340,000</div>
  <div class="photo photo--white" style="left:13px;top:829px" role="img" aria-label="Photo of a white two story home with fuel tanks"></div>
  <div class="listing listing--left" style="top:831px">
    <h2>2094 Hobart's Way</h2>
    <p class="lot">SF Lot: 10,250</p>
    <p>Fantastic 2 story located with the Whitcombe subdivision.<br>Unit #1 has 3 bedrooms, 1.5 bath's and 1,183 SF of living space.<br>Unit #2 has 2 bedrooms, 1.5 baths' and 967 SF of living space.</p>
  </div>

  <div class="web-bar"><span>www.tundrahomes.com</span></div>

  <div class="contact-title">Contact Info:</div>
  <div class="agent agent--left">
    <p>Gordon Dalby</p>
    <p>Office: (907) 413-2097</p>
    <p>Cell: (907) 356-1942</p>
    <p>Email: Gordon@TundraSell.com</p>
  </div>

  <div class="brokerage">
    <div class="brokerage-name"><i></i>NORTHWAY COMMERCIAL</div>
    <p class="brokerage-address">240 W. Alder Avenue, Suite 12, Anchorage, Alaska 99501</p>
  </div>

  <div class="agent agent--right">
    <p>Hattie Dalby</p>
    <p>Office: (907) 413-2097</p>
    <p>Cell: (907) 584-6071</p>
    <p>Email: Hattie@TundraSell.com</p>
  </div>
</div>
</body>
</html>
```